Mara Quennell Fitness

I need a web design for my nutrition/fitness training business. The name of the business is MQ Fitness. I sell fitness programs and do online personal training/nutritional coaching. What I promote right now is my 8 week program and i'm also coming out with a phase two 8 week program. I want to feature both, with coinvale links that way people can buy it through my website. I want the website designed around my logo with a black background. And tabs for my program, a tab for an about me section, a tab for me to post a blog, and a tab for my client testimonials/transformations. I want it to be pretty simple and easy to navigate through.
Target Market(s)
Fitness Industry
Industry/Entity Type
Fitness
Number of Pages Required
5+ page
Requirements
Must have
- I made a mock design and put it in the images. I want my website front page to be focused on my logo (which I attached) and also the tabs shown like I have it. Also need a play under my 8 week program tab to let people purchase my separate programs with coinvale. Under the blog I just need something that says "coming soon" on that page. And under the about me I attached a picture of my that I want (eating a donut lol) where I want to be able to put a bio next to it.

```html
<!DOCTYPE html>
<html lang="en">
<head>
<meta charset="utf-8">
<title>MQ Fitness</title>
<link href="https://fonts.googleapis.com/css2?family=Open+Sans:wght@400;600;700;800&display=swap" rel="stylesheet">
<style>
:root{
  --pink:#ee3f7a;
  --green:#6cc04a;
  --black:#0b0b0b;
  --panel:#1c1c1c;
  --line:#3a3a3a;
  --text:#d8d8d8;
  --muted:#8a8a8a;
  --white:#ffffff;
}
*{box-sizing:border-box;margin:0;padding:0}
html,body{width:1200px;height:3004px;overflow:hidden;background:var(--black);font-family:"Open Sans",Arial,sans-serif;color:var(--text)}
.page{position:relative;width:1200px;height:3004px}
.screen{position:absolute;left:0;width:1200px;overflow:hidden;border-bottom:4px solid #000}
.sidebar{position:absolute;left:0;top:0;bottom:0;width:210px;background:var(--black);padding:40px 0 0 24px}
.brand{display:flex;align-items:center;gap:10px;margin-left:6px}
.brand-dot{width:16px;height:16px;border-radius:50%;background:var(--pink)}
.brand-name{font-size:22px;font-weight:800;color:var(--green);line-height:1.1;width:130px}
.nav{list-style:none;margin-top:90px}
.nav li{font-size:11px;line-height:26px;color:var(--muted)}
.nav li.active{color:var(--pink)}
.social{display:flex;gap:10px;margin-top:96px}
.social span{width:24px;height:24px;border-radius:50%;border:1px solid #555}
.pay{margin-top:30px;font-size:10px;color:var(--muted)}
.pay b{font-size:15px;color:var(--white);font-weight:700;margin-left:4px}
.copyright{margin-top:34px;font-size:8px;color:#555}
.content{position:absolute;left:210px;top:0;right:0;bottom:0}
.backdrop{position:absolute;inset:0}
.hero .backdrop{background:linear-gradient(100deg,#2a2420 0%,#5c4c40 35%,#8a7460 60%,#3a3029 100%)}
.program .backdrop{background:linear-gradient(90deg,#1a1a1a 0%,#262626 50%,#4a4744 100%)}
.testimonials .backdrop{background:linear-gradient(180deg,#262626 0%,#1e1e1e 60%,#2a2826 100%)}
.about .backdrop{background:linear-gradient(180deg,#232323,#1a1a1a)}
.soon .backdrop{background:linear-gradient(160deg,#2a2a2a,#141414)}
.inner{position:absolute;left:70px;top:0;right:40px;bottom:0}
.hero h1{position:absolute;top:255px;font-size:40px;font-weight:700;color:var(--white)}
.hero p{position:absolute;top:312px;font-size:14px;color:var(--white)}
.btn{display:inline-block;font-size:12px;font-weight:700;color:var(--white);border-radius:18px;padding:10px 22px}
.btn-pink{background:var(--pink)}
.btn-green{background:var(--green)}
.hero .btn{position:absolute;top:352px}
.program-title{position:absolute;top:40px;display:flex;align-items:flex-end;gap:10px}
.program-title .num{font-size:140px;font-weight:800;color:var(--green);line-height:.9}
.program-title .label{font-size:26px;font-weight:700;color:var(--white);line-height:1.05;padding-bottom:10px}
.weeks{position:absolute;top:220px;left:0;display:grid;grid-template-columns:repeat(3,270px);column-gap:20px;row-gap:30px}
.week{display:flex;gap:12px;border:1px solid var(--line);height:96px;padding:8px}
.week-badge{width:78px;background:var(--pink);color:var(--white);display:flex;flex-direction:column;align-items:center;justify-content:center;font-size:9px;font-weight:700}
.week-badge strong{font-size:44px;line-height:1}
.week ul{list-style:none;font-size:9px;line-height:16px;color:var(--text);padding-top:6px}
.week li::before{content:"";display:inline-block;width:4px;height:4px;background:var(--pink);margin-right:6px;vertical-align:middle}
.book-cell{display:flex;align-items:center;justify-content:center}
.section-title{position:absolute;font-size:24px;font-weight:600;color:var(--white)}
.quote-mark{position:absolute;left:0;top:40px;width:90px;height:70px}
.testimonials .section-title{top:92px}
.quotes{position:absolute;top:160px;left:0;right:0;display:grid;grid-template-columns:1fr 1fr;column-gap:50px;row-gap:30px}
.quote{border:1px solid var(--line);padding:22px 26px;height:180px;background:rgba(0,0,0,.25)}
.quote p{font-size:11px;line-height:19px;color:var(--text);font-style:italic}
.quote cite{display:block;margin-top:22px;font-size:11px;font-style:normal;font-weight:700;color:var(--white)}
.about-photo{position:absolute;left:0;top:60px;width:410px;height:480px;background:linear-gradient(160deg,#bdbdbd 0%,#6e6e6e 45%,#2e2e2e 100%)}
.about-text{position:absolute;left:500px;top:40px;right:0}
.about-text h2{font-size:24px;font-weight:600;color:var(--white);margin-bottom:14px}
.about-text p{font-size:10.5px;line-height:17px;color:var(--text);margin-bottom:14px}
.signature{width:90px;height:36px;background:#3a3a3a;margin:6px 0 40px}
.contact{display:flex;justify-content:space-between;font-size:10px;color:var(--white);font-weight:600}
.soon .section-title{top:190px;font-size:22px}
</style>
</head>
<body>
<div class="page">

  <!-- Home -->
  <section class="screen hero" style="top:0;height:600px">
    <aside class="sidebar">
      <div class="brand"><span class="brand-dot"></span><span class="brand-name">MQ Fitness</span></div>
      <ul class="nav"><li class="active">Home</li><li>My 8 Week Program</li><li>Testimonials/Transformations</li><li>About Mara</li><li>Mara Blog</li></ul>
      <div class="social"><span></span><span></span><span></span><span></span></div>
      <div class="pay">Pay with<b>coinvale</b></div>
      <div class="copyright">Copyright © MQ Fitness</div>
    </aside>
    <div class="content">
      <div class="backdrop" role="img" aria-label="Woman seated cross-legged in a meditation pose by the water at sunset"></div>
      <div class="inner">
        <h1>Nutrition/ Fitness Training</h1>
        <p>I sell fitness programs and do online personal training/nutritional coaching</p>
        <a class="btn btn-pink">Book My Program</a>
      </div>
    </div>
  </section>

  <!-- Program -->
  <section class="screen program" style="top:600px;height:600px">
    <aside class="sidebar">
      <div class="brand"><span class="brand-dot"></span><span class="brand-name">MQ Fitness</span></div>
      <ul class="nav"><li>Home</li><li class="active">My 8 Week Program</li><li>Testimonials/Transformations</li><li>About Mara</li><li>Mara Blog</li></ul>
      <div class="social"><span></span><span></span><span></span><span></span></div>
      <div class="pay">Pay with<b>coinvale</b></div>
      <div class="copyright">Copyright © MQ Fitness</div>
    </aside>
    <div class="content">
      <div class="backdrop" role="img" aria-label="Dim living room with a sofa and lamp"></div>
      <div class="inner">
        <div class="program-title"><span class="num">8</span><span class="label">week<br>program</span></div>
        <div class="weeks">
          <div class="week"><div class="week-badge">WEEK<strong>1</strong></div><ul><li>Build a daily routine</li><li>Set your base meal plan</li><li>Track water and sleep</li></ul></div>
          <div class="week"><div class="week-badge">WEEK<strong>2</strong></div><ul><li>Add strength sessions</li><li>Balance your macros</li><li>Log every workout</li></ul></div>
          <div class="week"><div class="week-badge">WEEK<strong>3</strong></div><ul><li>Raise training volume</li><li>Prep meals ahead</li><li>Check in on progress</li></ul></div>
          <div class="week"><div class="week-badge">WEEK<strong>4</strong></div><ul><li>Introduce intervals</li><li>Refine portion sizes</li><li>Take progress photos</li></ul></div>
          <div class="week"><div class="week-badge">WEEK<strong>5</strong></div><ul><li>Push heavier lifts</li><li>Adjust your calories</li><li>Focus on recovery</li></ul></div>
          <div class="week"><div class="week-badge">WEEK<strong>6</strong></div><ul><li>Circuit training days</li><li>Smart snack swaps</li><li>Stretch every evening</li></ul></div>
          <div class="week"><div class="week-badge">WEEK<strong>7</strong></div><ul><li>Peak training block</li><li>Fine tune nutrition</li><li>Stay consistent</li></ul></div>
          <div class="week"><div class="week-badge">WEEK<strong>8</strong></div><ul><li>Final strength test</li><li>Plan your next phase</li><li>Celebrate results</li></ul></div>
          <div class="book-cell"><a class="btn btn-green">Book My Program</a></div>
        </div>
      </div>
    </div>
  </section>

  <!-- Testimonials -->
  <section class="screen testimonials" style="top:1200px;height:620px">
    <aside class="sidebar">
      <div class="brand"><span class="brand-dot"></span><span class="brand-name">MQ Fitness</span></div>
      <ul class="nav"><li>Home</li><li>My 8 Week Program</li><li class="active">Testimonials/Transformations</li><li>About Mara</li><li>Mara Blog</li></ul>
      <div class="social"><span></span><span></span><span></span><span></span></div>
      <div class="pay">Pay with<b>coinvale</b></div>
      <div class="copyright">Copyright © MQ Fitness</div>
    </aside>
    <div class="content">
      <div class="backdrop" role="img" aria-label="Dark gym interior with training equipment"></div>
      <div class="inner">
        <svg class="quote-mark" viewBox="0 0 90 70" aria-hidden="true"><path d="M10 70V40Q10 10 38 4l3 8Q24 18 24 36h16v34zM52 70V40Q52 10 80 4l3 8Q66 18 66 36h16v34z" fill="#ffffff" opacity=".06"/></svg>
        <h2 class="section-title">Testimonials/ Transformations</h2>
        <div class="quotes">
          <div class="quote"><p>"The program gave me structure I never had before. I lost weight, gained strength and finally enjoy cooking healthy meals every single week."</p><cite>Happy client</cite></div>
          <div class="quote"><p>"Clear workouts, simple food plans and real support every week. Eight weeks later I feel stronger and more confident than I have in years."</p><cite>Happy client</cite></div>
          <div class="quote"><p>"I was nervous to start but every step was explained well. My energy is up, my clothes fit better and the habits have stuck with me."</p><cite>Happy client</cite></div>
          <div class="quote"><p>"Online coaching fit right into my busy schedule. The check ins kept me on track and the results speak for themselves. Highly recommend it."</p><cite>Happy client</cite></div>
        </div>
      </div>
    </div>
  </section>

  <!-- About -->
  <section class="screen about" style="top:1820px;height:600px">
    <aside class="sidebar">
      <div class="brand"><span class="brand-dot"></span><span class="brand-name">MQ Fitness</span></div>
      <ul class="nav"><li>Home</li><li>My 8 Week Program</li><li>Testimonials/Transformations</li><li class="active">About Mara</li><li>Mara Blog</li></ul>
      <div class="social"><span></span><span></span><span></span><span></span></div>
      <div class="pay">Pay with<b>coinvale</b></div>
      <div class="copyright">Copyright © MQ Fitness</div>
    </aside>
    <div class="content">
      <div class="backdrop"></div>
      <div class="inner">
        <div class="about-photo" role="img" aria-label="Black and white photo of the trainer standing beside a truck eating a donut"></div>
        <div class="about-text">
          <h2>About Mara</h2>
          <p>Fitness has been part of my life for as long as I can remember. After years of training myself and helping friends reach their goals, I turned that passion into a career as a personal trainer and nutrition coach. I believe healthy living should be simple, balanced and enjoyable, which is why my programs focus on real food, smart training and habits that last well beyond eight weeks.</p>
          <p>Every plan I write is built around your life, your schedule and your goals. Whether you want to lose fat, build strength or just feel better every day, I will guide you with clear workouts, easy meal plans and honest weekly check ins. And yes, there is still room for the occasional donut. Let's get started together today.</p>
          <div class="signature" role="img" aria-label="Handwritten signature"></div>
          <div class="contact"><span>Contact: 1800 555 0142</span><span>Email: hello@mqfitness.com</span></div>
        </div>
      </div>
    </div>
  </section>

  <!-- Blog -->
  <section class="screen soon" style="top:2420px;height:584px">
    <aside class="sidebar">
      <div class="brand"><span class="brand-dot"></span><span class="brand-name">MQ Fitness</span></div>
      <ul class="nav"><li>Home</li><li>My 8 Week Program</li><li>Testimonials/Transformations</li><li>About Mara</li><li class="active">Mara Blog</li></ul>
      <div class="social"><span></span><span></span><span></span><span></span></div>
      <div class="pay">Pay with<b>coinvale</b></div>
      <div class="copyright">Copyright © MQ Fitness</div>
    </aside>
    <div class="content">
      <div class="backdrop"></div>
      <div class="inner">
        <h2 class="section-title">Coming Soon</h2>
      </div>
    </div>
  </section>

</div>
</body>
</html>
```